Postcard Design for Thank Yous

I am a Voice Actor and want to send personal thank you cards or postcards to clients after recording sessions. the basic concept is front art that simply has background art & my logo (sample below but wrong size), and the other side would be space for mailing address as well as a small version of my logo and contact info and of course plenty of blank space for me to write a personal message. I am open to your opinion as to whether a postcard, or a card and mailing envelope makes more sense. (I am also including the back of business card as example of contact listing, but one number will not be included and I might want to change other verbiage). Thank you! -Neil

```html
<!DOCTYPE html>
<html lang="en">
<head>
<meta charset="utf-8">
<title>Neil Harwood – Thank You Postcard</title>
<link rel="stylesheet" href="https://fonts.googleapis.com/css2?family=Mulish:wght@700;800;900&display=swap">
<style>
  :root {
    --page: #e9e6e1;
    --ink: #1b1b1b;
    --brand-red: #e0202a;
    --white: #ffffff;
    --stamp: #b9b9b9;
    --rule: #bdbdbd;
    --muted: #8a8a8a;
  }
  * { margin: 0; padding: 0; box-sizing: border-box; }
  html, body { width: 900px; height: 1200px; overflow: hidden; }
  body {
    position: relative;
    background: var(--page);
    font-family: "Mulish", "Helvetica Neue", Arial, sans-serif;
  }
  .postcard {
    position: absolute;
    left: 96px;
    width: 708px;
    overflow: hidden;
  }
  .postcard--front { top: 40px; height: 548px; background: #0a0a0a; }
  .postcard--back { top: 610px; height: 550px; background: var(--white); }

  /* front photo area: poker table tones */
  .front-art {
    position: absolute; inset: 0;
    background:
      radial-gradient(ellipse 38% 22% at 48% 50%, rgba(225,225,225,.55) 0%, rgba(225,225,225,0) 100%),
      radial-gradient(ellipse 22% 26% at 12% 62%, rgba(190,190,190,.45) 0%, rgba(190,190,190,0) 100%),
      radial-gradient(ellipse 20% 22% at 90% 24%, rgba(200,200,200,.45) 0%, rgba(200,200,200,0) 100%),
      radial-gradient(ellipse at 45% 35%, #7a7a7a 0%, #4d4d4d 35%, #262626 65%, #0a0a0a 100%);
  }
  .front-art::after {
    content: ""; position: absolute; inset: 0;
    background: linear-gradient(to bottom, rgba(0,0,0,0) 50%, rgba(0,0,0,.92) 92%);
  }
  .brand-block {
    position: absolute;
    left: 532px; top: 390px;
    width: 116px;
    display: flex; flex-direction: column; align-items: center;
  }
  .brand-square {
    width: 56px; height: 56px;
    background: var(--brand-red);
  }
  .brand-name {
    margin-top: 10px;
    color: var(--white);
    font-size: 17px; font-weight: 800;
    white-space: nowrap;
  }
  .brand-url {
    margin-top: 2px;
    color: var(--muted);
    font-size: 8px; font-weight: 700;
  }

  /* back faded photo */
  .back-art {
    position: absolute; inset: 0;
    background:
      radial-gradient(ellipse 30% 45% at 10% 80%, rgba(175,175,175,.55) 0%, rgba(175,175,175,0) 100%),
      radial-gradient(ellipse 40% 22% at 50% 58%, rgba(205,205,205,.5) 0%, rgba(205,205,205,0) 100%),
      radial-gradient(ellipse 25% 20% at 80% 10%, rgba(200,200,200,.45) 0%, rgba(200,200,200,0) 100%),
      linear-gradient(to right, #ececec 0%, #f7f7f7 60%, #fbfbfb 100%);
  }
  .contact {
    position: absolute; left: 42px; top: 34px;
  }
  .contact__name {
    color: var(--brand-red);
    font-size: 34px; font-weight: 900;
    letter-spacing: .8px; line-height: 1.1;
    white-space: nowrap;
  }
  .contact__title {
    display: block;
    margin-top: 8px;
    width: 335px; height: 38px;
    background: var(--ink);
    color: var(--white);
    font-size: 27px; font-weight: 800;
    letter-spacing: 9px;
    padding-left: 9px;
    line-height: 38px;
    text-align: center;
    white-space: nowrap;
  }
  .contact__list {
    list-style: none;
    margin-top: 18px;
    color: var(--ink);
    font-size: 16px; font-weight: 800;
    letter-spacing: .4px;
    line-height: 22.5px;
    white-space: nowrap;
  }
  .contact__label { color: var(--brand-red); }
  .stamp-box {
    position: absolute; left: 590px; top: 31px;
    width: 86px; height: 86px;
    background: var(--stamp);
  }
  .address-lines {
    position: absolute; left: 454px; top: 373px;
    width: 222px;
  }
  .address-lines span {
    display: block; height: 2px;
    background: var(--rule);
    margin-bottom: 35px;
  }
  .back-brand {
    position: absolute; left: 42px; top: 500px;
    display: flex; align-items: center; gap: 8px;
  }
  .back-brand__square {
    width: 18px; height: 18px;
    background: var(--brand-red);
  }
  .back-brand__name {
    color: var(--ink);
    font-size: 13px; font-weight: 800;
  }
</style>
</head>
<body>
  <section class="postcard postcard--front">
    <div class="front-art" role="img" aria-label="Black and white photo of a poker table with an ace, king and two face up among stacks of chips"></div>
    <div class="brand-block">
      <div class="brand-square"></div>
      <p class="brand-name">Neil Harwood</p>
      <p class="brand-url">neilharwoodvoice.com</p>
    </div>
  </section>

  <section class="postcard postcard--back">
    <div class="back-art" role="img" aria-label="Faded light grey poker table photo with cards and chip stacks"></div>
    <div class="contact">
      <h1 class="contact__name">NEIL HARWOOD</h1>
      <p class="contact__title">VOICE ACTOR</p>
      <ul class="contact__list">
        <li>www.neilharwoodvoice.com</li>
        <li>Session Link / ISDN Ready</li>
        <li><span class="contact__label">Office-</span> 555.210.4471</li>
        <li><span class="contact__label">Cell-</span> 555.318.6620</li>
        <li><span class="contact__label">Studio phone patch-</span> 555.742.0938</li>
        <li>neil@neilharwoodvoice.com</li>
      </ul>
    </div>
    <div class="stamp-box"></div>
    <div class="address-lines"><span></span><span></span><span></span></div>
    <div class="back-brand">
      <div class="back-brand__square"></div>
      <p class="back-brand__name">Neil Harwood</p>
    </div>
  </section>
</body>
</html>
```